PPT template for BLQ. Whiskey, wine, food, drink and music. Moments in time

Lantern Oak and Barrels. Liquor, food, music. Need slides for BLQ, Liquor, food and music.

Think whiskey distillery meets music studio.

Its about moments in time with the people we love. Music, food and drink all play apart in the times we remember.

Target Market(s)

Investors

Industry/Entity Type

Entertainment

Colors

Designer to choose colors to be used in the design.

Requirements
Must have
• Utilize the logo or image without text in all slides.
Nice to have
• blank template pages with logo or just image. multiple versions I can utilize. Logo and image as backgrounds, logo in corner and so on. Logo in many colors, rainbow, nautilus shell. Golden ratio....
Should not have
• Do not need close ups of food. its about people and experiences and food is part of this. Think tables, parties, events, chocolate fountains, and so on

```html
<!DOCTYPE html>
<html lang="en">
<head>
<meta charset="utf-8">
<title>Lantern Oak and Barrels — Presentation Template</title>
<link href="https://fonts.googleapis.com/css2?family=Cinzel:wght@400;700&family=Open+Sans:wght@400;600;700&display=swap" rel="stylesheet">
<style>
:root{
  --navy:#2b2c86;
  --navy-deep:#16144a;
  --navy-mid:#2a2877;
  --ink:#3a3a3a;
  --grey-dark:#444446;
  --grey:#8c8c90;
  --paper:#ffffff;
  --board:#d9d9db;
  --line-grey:#666;
}
*{box-sizing:border-box;margin:0;padding:0}
html,body{width:700px;height:1200px;overflow:hidden;background:var(--board)}
.canvas{position:relative;width:700px;height:1200px;overflow:hidden;background:var(--board)}
.slide{position:absolute;background:var(--paper);overflow:hidden}
.slide>*{position:absolute}
.photo{display:block}
.title{font-family:'Cinzel',serif;color:var(--navy);font-size:8px;letter-spacing:.3px;white-space:nowrap;line-height:1}
.title.light{color:var(--paper)}
.rule{height:1.2px;width:9px;background:var(--navy)}
.rule.light{background:var(--paper)}
.copy{font-family:'Open Sans',sans-serif;font-size:3.2px;line-height:4.9px;color:var(--ink)}
.copy.light{color:var(--paper)}
.copy.navy{color:var(--navy)}
.btn{font-family:'Open Sans',sans-serif;font-weight:700;font-size:3.1px;letter-spacing:.8px;color:var(--navy);border:.7px solid var(--navy);padding:1.2px 1.8px;line-height:1}
.btn.light{color:var(--paper);border-color:var(--paper)}
.spine{width:1.8px;background:var(--navy)}
.spine.light{background:var(--paper)}
.badge{width:18px;height:18px;border-radius:50%;background:var(--paper);border:1.8px solid var(--navy)}
.badge.light{border-color:var(--paper);background:transparent}
.dot{width:6px;height:6px;border-radius:50%;background:var(--navy)}
.dot.light{background:var(--paper)}
.disc{width:26px;height:26px;border-radius:50%;background:var(--navy);display:flex;align-items:center;justify-content:center}
.disc::before{content:"";position:absolute;inset:2px;border:.7px solid var(--paper);border-radius:50%}
.disc svg{width:13px;height:13px;stroke:var(--paper);fill:none;stroke-width:1.6;stroke-linecap:round;stroke-linejoin:round}
.wordmark{font-family:'Cinzel',serif;font-weight:400;color:var(--navy);text-align:center;line-height:1;white-space:nowrap}
.wordmark .name{display:block;font-size:6px;letter-spacing:2.2px}
.wordmark .sub{display:block;font-size:2.6px;letter-spacing:1.3px;margin-top:1px}
.wordmark.light{color:var(--paper)}
.mark{border-radius:50%;border:1.4px solid var(--navy)}
.mark.light{border-color:var(--paper)}
.blob{left:0;top:0;width:100%;height:100%}
.info-head{font-family:'Open Sans',sans-serif;font-weight:700;font-size:7.4px;color:var(--navy);line-height:1.2}
.info-copy{font-family:'Open Sans',sans-serif;font-size:7px;line-height:10.2px;color:var(--ink)}
.info-disc{width:48px;height:48px;border-radius:50%;background:var(--navy);display:flex;align-items:center;justify-content:center}
.info-disc::before{content:"";position:absolute;inset:4px;border:1.6px solid var(--paper);border-radius:50%}
.info-disc svg{width:22px;height:22px;stroke:var(--paper);fill:none;stroke-width:1.6;stroke-linecap:round;stroke-linejoin:round}
.card{width:61px;height:74px;border-radius:8px}
.card .copy{position:absolute;left:5px;right:5px;top:26px;text-align:center;color:var(--paper);font-size:3.1px;line-height:4.7px}
.card-disc{width:26px;height:26px;border-radius:50%;border:1.4px solid var(--paper);display:flex;align-items:center;justify-content:center}
.card-disc svg{width:13px;height:13px;stroke:var(--paper);fill:none;stroke-width:1.6;stroke-linecap:round;stroke-linejoin:round}
.bullets{list-style:none;font-family:'Open Sans',sans-serif;font-size:3.2px;line-height:4.9px;color:var(--ink)}
.bullets li{position:relative;padding-left:6px;margin-bottom:5.4px}
.bullets li::before{content:"";position:absolute;left:0;top:1.5px;width:2.2px;height:2.2px;border-radius:50%;background:var(--navy)}
.social{width:12px;height:12px;border-radius:50%;border:.9px solid var(--paper)}
.contact{font-family:'Open Sans',sans-serif;font-size:3px;color:var(--paper);display:flex;align-items:center;gap:2px;line-height:1.3}
.contact svg{width:6px;height:6px;stroke:var(--paper);fill:none;stroke-width:1.6;flex:none}
</style>
</head>
<body>
<svg width="0" height="0" style="position:absolute" aria-hidden="true">
  <symbol id="i-apple" viewBox="0 0 24 24"><path d="M12 7c-2-2-7-1.5-7 4 0 5 3 9 5 9 1 0 1.3-.6 2-.6s1 .6 2 .6c2 0 5-4 5-9 0-5.5-5-6-7-4z"/><path d="M12 7c0-2 1-3.5 3-4"/></symbol>
  <symbol id="i-flame" viewBox="0 0 24 24"><path d="M12 3c1 4 6 6 6 11a6 6 0 0 1-12 0c0-3 2-4 2-6 2 1 3 3 3 5 1-2 1-6 1-10z"/></symbol>
  <symbol id="i-drops" viewBox="0 0 24 24"><path d="M8 6c-2 4-4 6-4 8.5a4 4 0 0 0 8 0C12 12 10 10 8 6z"/><path d="M16 6c-2 4-4 6-4 8.5a4 4 0 0 0 8 0C20 12 18 10 16 6z"/></symbol>
  <symbol id="i-leaf" viewBox="0 0 24 24"><path d="M12 3l2 4 3-1-1 4 4 1-3 3 1 3-4-1-2 3-2-3-4 1 1-3-3-3 4-1-1-4 3 1z"/><path d="M12 14v7"/></symbol>
  <symbol id="i-notes" viewBox="0 0 24 24"><path d="M9 18V6l11-2v12"/><circle cx="6.5" cy="18" r="2.5"/><circle cx="17.5" cy="16" r="2.5"/></symbol>
  <symbol id="i-move" viewBox="0 0 24 24"><circle cx="15" cy="4" r="1.8"/><path d="M14 7l-3 5 4 3-1 6M11 12l-5 2M13 8l5 2M15 15l4 1"/></symbol>
  <symbol id="i-piano" viewBox="0 0 24 24"><path d="M4 10h16v8H4zM8 10v8M12 10v8M16 10v8M6 10V6h10l4 4"/></symbol>
  <symbol id="i-globe" viewBox="0 0 24 24"><circle cx="12" cy="12" r="9"/><path d="M3 12h18M12 3c3 3 3 15 0 18M12 3c-3 3-3 15 0 18"/></symbol>
  <symbol id="i-phone" viewBox="0 0 24 24"><path d="M5 4h4l2 5-2.5 1.5a11 11 0 0 0 5 5L15 13l5 2v4a2 2 0 0 1-2 2A16 16 0 0 1 3 6a2 2 0 0 1 2-2z"/></symbol>
  <symbol id="i-mail" viewBox="0 0 24 24"><path d="M3 6h18v12H3z"/><path d="M3 6l9 7 9-7"/></symbol>
  <symbol id="i-pin" viewBox="0 0 24 24"><path d="M12 21s-7-6-7-11a7 7 0 0 1 14 0c0 5-7 11-7 11z"/><circle cx="12" cy="10" r="2.5"/></symbol>
</svg>

<main class="canvas">

  <!-- Cover: white title -->
  <section class="slide slide-cover-white" style="left:7px;top:7px;width:223px;height:126px">
    <div style="left:0;top:3px;width:223px;height:1.4px;background:var(--navy)"></div>
    <div style="left:0;top:121px;width:223px;height:1.4px;background:var(--navy)"></div>
    <div class="mark" style="left:100px;top:32px;width:22px;height:22px;border-width:2px"></div>
    <div class="wordmark" style="left:0;width:223px;top:61px"><span class="name" style="font-size:11px;letter-spacing:5px">LANTERN OAK</span><span class="sub" style="font-size:3.6px;letter-spacing:2.4px;margin-top:2px">AND BARRELS</span></div>
    <div class="copy" style="left:0;width:223px;top:101px;text-align:center;font-size:4.4px;color:var(--navy);font-weight:600">2020</div>
  </section>

  <!-- Presentation title -->
  <section class="slide slide-presentation-title" style="left:7px;top:140px;width:223px;height:126px">
    <div class="photo" role="img" aria-label="Round photo of a warm table gathering with golden light" style="left:13px;top:28px;width:78px;height:68px;border-radius:50%;background:radial-gradient(circle at 60% 45%,#e6b858 0%,#b48a47 35%,#8fb9c0 75%,#cfe3e5 100%)"></div>
    <div class="spine" style="left:111px;top:15px;height:97px"></div>
    <div class="title" style="right:12px;top:17px;text-align:right;font-size:10px;line-height:13px">PRESENTATION<br>TITLE</div>
    <div class="rule" style="right:12px;top:44px;width:12px"></div>
    <div class="copy" style="right:12px;top:53px;font-size:5.6px;line-height:7px;color:var(--navy)">Subtitle goes here</div>
    <div class="mark" style="left:181px;top:90px;width:9px;height:9px;border-width:1.2px"></div>
    <div class="wordmark" style="left:154px;width:64px;top:103px"><span class="name" style="font-size:5px;letter-spacing:1.8px">LANTERN OAK</span><span class="sub" style="font-size:2.2px">AND BARRELS</span></div>
  </section>

  <!-- Main dark cover -->
  <section class="slide slide-cover-dark" style="left:238px;top:7px;width:454px;height:259px;background:radial-gradient(ellipse at 45% 25%,#38338f 0%,#241f6a 45%,#120f3c 100%)">
    <div class="social" style="left:408px;top:7px"></div>
    <div class="social" style="left:422px;top:7px"></div>
    <div class="social" style="left:436px;top:7px"></div>
    <div class="mark light" style="left:189px;top:70px;width:78px;height:78px;border-width:5px"></div>
    <div class="wordmark light" style="left:0;width:454px;top:158px"><span class="name" style="font-size:26px;letter-spacing:13px;padding-left:13px">LANTERN OAK</span><span class="sub" style="font-size:8.6px;letter-spacing:7px;margin-top:4px;padding-left:7px">AND BARRELS</span></div>
    <div class="copy light" style="left:0;width:454px;top:244px;text-align:center;font-size:6.4px;letter-spacing:4.2px;line-height:1">WWW.YOURWEBSITE.COM</div>
  </section>

  <!-- Food (blob) -->
  <section class="slide slide-food-feature" style="left:7px;top:273px;width:223px;height:126px">
    <div class="photo" role="img" aria-label="Photo of a shared brunch table with fresh dishes" style="left:0;top:0;width:223px;height:126px;background:linear-gradient(135deg,#4c5a3a 0%,#8e9a48 30%,#e3b542 50%,#b9873f 65%,#2c3a33 100%)"></div>
    <svg class="blob" viewBox="0 0 223 126" aria-hidden="true"><path d="M0 0C12 20 40 40 60 70C75 95 80 110 90 126L0 126Z" fill="var(--navy)"/><path d="M140 0C132 30 160 50 178 78C190 100 205 115 223 120L223 0Z" fill="var(--navy)" opacity=".92"/></svg>
    <div class="title light" style="right:7px;top:9px">FOOD</div>
    <div class="copy light" style="right:7px;top:23px;width:44px;text-align:right">Lorem ipsum dolor sit amet, consectetuer adipiscing elit, sed diam nonummy nibh euismod tincidunt ut laoreet dolore magna aliquam</div>
    <div class="disc" style="left:183px;top:69px"><svg><use href="#i-apple"/></svg></div>
    <div class="mark light" style="left:33px;top:89px;width:9px;height:9px"></div>
    <div class="wordmark light" style="left:6px;width:64px;top:101px"><span class="name" style="font-size:5px;letter-spacing:1.8px">LANTERN OAK</span><span class="sub" style="font-size:2.2px">AND BARRELS</span></div>
  </section>

  <!-- Logo title -->
  <section class="slide slide-brand-title" style="left:238px;top:273px;width:223px;height:126px">
    <div class="mark" style="left:3px;top:-4px;width:134px;height:134px;border:10px solid var(--navy)"></div>
    <div class="mark" style="left:173px;top:20px;width:8px;height:8px;border-width:1.2px"></div>
    <div class="wordmark" style="left:146px;width:64px;top:32px"><span class="name" style="font-size:5px;letter-spacing:1.8px">LANTERN OAK</span><span class="sub" style="font-size:2.2px">AND BARRELS</span></div>
    <div style="left:148px;top:53px;width:66px;height:1.2px;background:var(--navy)"></div>
    <div class="title" style="left:148px;width:66px;top:66px;text-align:center;font-size:10px">TITLE</div>
    <div class="copy" style="left:148px;width:66px;top:80px;text-align:center">Lorem ipsum dolor sit amet, consectetuer adipiscing elit, sed diam nonummy nibh euismod tincidunt ut laoreet dolore magna aliquam erat volutpat. Ut wisi enim ad minim veniam, quis nostrud exerci tation ullamcorper suscipit lobortis nisl ut</div>
  </section>

  <!-- Liquor -->
  <section class="slide slide-liquor" style="left:469px;top:273px;width:223px;height:126px">
    <div class="spine" style="left:12px;top:0;height:126px"></div>
    <div class="badge" style="left:3px;top:9px"></div>
    <div class="title" style="left:27px;top:15px">LIQUOR</div>
    <div class="rule" style="left:27px;top:27px"></div>
    <div class="copy" style="left:27px;top:38px;width:62px">Lorem ipsum dolor sit amet, consectetuer adipiscing elit, sed diam nonummy nibh euismod tincidunt ut laoreet dolore magna aliquam erat volutpat. Ut wisi enim ad minim veniam, quis nostrud exerci tation ullamcorper suscipit lobortis nisl ut aliquip ex ea commodo consequat. Duis autem vel eum iriure dolor in hendrerit</div>
    <div class="btn" style="left:27px;top:96px">LEARN MORE</div>
    <div class="photo" role="img" aria-label="Round photo of whiskey being poured over ice" style="left:113px;top:9px;width:102px;height:102px;border-radius:50%;background:radial-gradient(circle at 50% 55%,#e39a3a 0%,#b86a1e 35%,#3a2312 75%,#1a120b 100%)"></div>
    <div class="disc" style="left:112px;top:82px"><svg><use href="#i-drops"/></svg></div>
    <div class="dot" style="left:211px;top:115px"></div>
  </section>

  <!-- Food (split) -->
  <section class="slide slide-food" style="left:7px;top:406px;width:223px;height:126px">
    <div class="photo" role="img" aria-label="Photo of colourful party desserts laid out on a table" style="left:13px;top:0;width:91px;height:113px;background:linear-gradient(160deg,#f3ede6 0%,#e9a98c 30%,#d9c072 55%,#b96b8e 80%,#efe7df 100%)"></div>
    <div style="left:88px;top:102px;width:18px;height:18px;background:var(--navy)"></div>
    <div class="title" style="left:129px;top:15px">FOOD</div>
    <div class="rule" style="left:129px;top:27px"></div>
    <div class="copy" style="left:129px;top:38px;width:62px">Lorem ipsum dolor sit amet, consectetuer adipiscing elit, sed diam nonummy nibh euismod tincidunt ut laoreet dolore magna aliquam erat volutpat. Ut wisi enim ad minim veniam, quis nostrud exerci tation ullamcorper suscipit lobortis nisl ut aliquip ex ea commodo consequat. Duis autem vel eum iriure dolor in hendrerit</div>
    <div class="btn" style="left:129px;top:96px">LEARN MORE</div>
    <div class="spine" style="left:209px;top:0;height:126px"></div>
    <div class="badge" style="left:201px;top:9px"></div>
    <div class="dot" style="left:4px;top:115px"></div>
  </section>

  <!-- Music -->
  <section class="slide slide-music" style="left:238px;top:406px;width:223px;height:126px">
    <div class="spine" style="left:12px;top:0;height:126px"></div>
    <div class="badge" style="left:3px;top:9px"></div>
    <div class="title" style="left:27px;top:15px">MUSIC</div>
    <div class="rule" style="left:27px;top:27px"></div>
    <div class="copy" style="left:27px;top:38px;width:62px">Lorem ipsum dolor sit amet, consectetuer adipiscing elit, sed diam nonummy nibh euismod tincidunt ut laoreet dolore magna aliquam erat volutpat. Ut wisi enim ad minim veniam, quis nostrud exerci tation ullamcorper suscipit lobortis nisl ut aliquip ex ea commodo consequat. Duis autem vel eum iriure dolor in hendrerit</div>
    <div class="btn" style="left:27px;top:96px">LEARN MORE</div>
    <svg class="photo" role="img" aria-label="Photo of sheet music resting on piano keys" viewBox="0 0 223 126" style="left:0;top:0;width:223px;height:126px"><defs><linearGradient id="g-sheet" x1="0" y1="0" x2="1" y2="1"><stop offset="0" stop-color="#f6dcc4"/><stop offset=".6" stop-color="#e8c3a6"/><stop offset="1" stop-color="#5a4a40"/></linearGradient></defs><path d="M98 0L223 0L223 126L140 126C150 110 120 105 118 90C116 75 130 70 126 55C122 40 100 38 104 22C106 12 98 8 98 0Z" fill="url(#g-sheet)"/></svg>
    <div class="disc" style="left:93px;top:87px"><svg><use href="#i-notes"/></svg></div>
    <div class="dot" style="left:213px;top:115px"></div>
  </section>

  <!-- BLQ -->
  <section class="slide slide-blq" style="left:469px;top:406px;width:223px;height:126px">
    <div class="photo" role="img" aria-label="Photo of a person stretching on a rocky seashore" style="left:26px;top:0;width:85px;height:126px;background:linear-gradient(180deg,#c9cdd1 0%,#9aa4ad 35%,#6f6760 60%,#8c7b6b 100%)"></div>
    <div class="disc" style="left:13px;top:40px"><svg><use href="#i-move"/></svg></div>
    <div class="title" style="left:129px;top:15px">BLQ</div>
    <div class="rule" style="left:129px;top:27px"></div>
    <div class="copy" style="left:129px;top:38px;width:62px">Lorem ipsum dolor sit amet, consectetuer adipiscing elit, sed diam nonummy nibh euismod tincidunt ut laoreet dolore magna aliquam erat volutpat. Ut wisi enim ad minim veniam, quis nostrud exerci tation ullamcorper suscipit lobortis nisl ut aliquip ex ea commodo consequat. Duis autem vel eum iriure dolor in hendrerit</div>
    <div class="btn" style="left:129px;top:96px">LEARN MORE</div>
    <div class="spine" style="left:210px;top:0;height:126px"></div>
    <div class="badge" style="left:201px;top:9px"></div>
    <div class="dot" style="left:4px;top:115px"></div>
  </section>

  <!-- Spirits -->
  <section class="slide slide-spirits" style="left:7px;top:539px;width:223px;height:126px">
    <div class="photo" role="img" aria-label="Photo of a white bird in flight against a dark city wall" style="left:0;top:0;width:223px;height:126px;background:radial-gradient(ellipse at 70% 55%,#8a8884 0%,#5a5a5a 30%,#3b3c3d 70%,#2c2d2e 100%)"></div>
    <div class="spine light" style="left:12px;top:0;height:126px"></div>
    <div class="badge light" style="left:3px;top:9px;background:var(--paper);border-color:var(--paper)"></div>
    <div class="title light" style="left:27px;top:15px">SPIRITS</div>
    <div class="rule light" style="left:27px;top:27px"></div>
    <div class="copy light" style="left:27px;top:38px;width:62px">Lorem ipsum dolor sit amet, consectetuer adipiscing elit, sed diam nonummy nibh euismod tincidunt ut laoreet dolore magna aliquam erat volutpat. Ut wisi enim ad minim veniam, quis nostrud exerci tation ullamcorper suscipit lobortis nisl ut aliquip ex ea commodo consequat. Duis autem vel eum iriure dolor in hendrerit</div>
    <div class="btn light" style="left:27px;top:96px">LEARN MORE</div>
    <div class="dot light" style="left:213px;top:115px"></div>
  </section>

  <!-- About us -->
  <section class="slide slide-about" style="left:238px;top:539px;width:223px;height:126px">
    <div class="spine" style="left:12px;top:0;height:126px"></div>
    <div class="badge" style="left:3px;top:9px"></div>
    <div class="title" style="left:27px;top:15px">ABOUT US</div>
    <div class="rule" style="left:27px;top:27px"></div>
    <div class="copy" style="left:22px;top:38px;width:62px">Lorem ipsum dolor sit amet, consectetuer adipiscing elit, sed diam nonummy nibh euismod tincidunt ut laoreet dolore magna aliquam erat volutpat.<br><br>Ut wisi enim ad minim veniam, quis nostrud exerci tation ullamcorper suscipit lobortis nisl ut aliquip ex ea commodo consequat. Duis autem vel eum iriure dolor in hendrerit</div>
    <div class="photo" role="img" aria-label="Photo of a person balancing on a rock at sunset" style="left:92px;top:22px;width:56px;height:84px;background:linear-gradient(180deg,#f1dcc0 0%,#d9b58a 50%,#4a3a2c 85%,#2e241c 100%)"></div>
    <div class="photo" role="img" aria-label="Photo of stacked stones on a green background" style="left:151px;top:22px;width:65px;height:43px;background:radial-gradient(circle at 50% 60%,#3a3a36 0%,#4c6b3a 40%,#7fa05a 100%)"></div>
    <div style="left:151px;top:67px;width:65px;height:39px;background:#2b2b2d"></div>
    <div class="mark light" style="left:179px;top:73px;width:9px;height:9px"></div>
    <div class="wordmark light" style="left:151px;width:65px;top:86px"><span class="name" style="font-size:5.4px;letter-spacing:1.6px">LANTERN OAK</span><span class="sub" style="font-size:2.4px">AND BARRELS</span></div>
    <div class="dot" style="left:213px;top:115px"></div>
  </section>

  <!-- Our dream -->
  <section class="slide slide-dream" style="left:469px;top:539px;width:223px;height:126px">
    <div class="photo" role="img" aria-label="Photo of a person relaxing on a beach at sunset" style="left:0;top:0;width:223px;height:126px;background:linear-gradient(180deg,#4c6b93 0%,#8796a8 25%,#e9a551 48%,#c7722b 58%,#4a4038 80%,#2b2622 100%)"></div>
    <svg class="blob" viewBox="0 0 223 126" aria-hidden="true"><path d="M196 0C176 40 178 90 202 126L223 126L223 0Z" fill="var(--navy)" opacity=".85"/></svg>
    <div class="spine light" style="left:12px;top:0;height:126px"></div>
    <div class="badge light" style="left:3px;top:9px;background:var(--paper);border-color:var(--paper)"></div>
    <div class="title light" style="left:27px;top:15px">OUR DREAM</div>
    <div class="rule light" style="left:27px;top:27px"></div>
    <div class="copy light" style="left:22px;top:38px;width:62px">Lorem ipsum dolor sit amet, consectetuer adipiscing elit, sed diam nonummy nibh euismod tincidunt ut laoreet dolore magna aliquam erat volutpat.<br><br>Ut wisi enim ad minim veniam, quis nostrud exerci tation ullamcorper suscipit lobortis nisl ut aliquip ex ea commodo consequat. Duis autem vel eum iriure dolor in hendrerit</div>
    <div class="dot light" style="left:214px;top:115px"></div>
  </section>

  <!-- What we do -->
  <section class="slide slide-what-we-do" style="left:7px;top:672px;width:223px;height:126px">
    <div style="left:6px;top:6px;width:211px;height:114px;border:1.2px solid var(--navy)"></div>
    <div style="left:0;top:34px;width:223px;height:58px;background:var(--navy)"></div>
    <div class="title light" style="left:0;width:223px;top:42px;text-align:center">WHAT WE DO</div>
    <div class="rule light" style="left:107px;top:54px"></div>
    <div class="copy light" style="left:30px;width:163px;top:63px;text-align:center">Lorem ipsum dolor sit amet, consectetuer adipiscing elit, sed diam nonummy nibh euismod tincidunt ut laoreet dolore magna aliquam erat volutpat. Ut wisi enim ad minim veniam, quis nostrud exerci tation ullamcorper suscipit lobortis nisl ut aliquip ex ea commodo consequat. Duis autem vel eum iriure dolor in hendrerit</div>
  </section>

  <!-- Three cards -->
  <section class="slide slide-cards" style="left:238px;top:672px;width:223px;height:126px">
    <div class="title" style="left:0;width:223px;top:9px;text-align:center">LOREM IPSUM DOLOR</div>
    <div class="card" style="left:10px;top:39px;background:var(--navy)"><div class="copy">Lorem ipsum dolor sit amet, consectetuer adipiscing elit, sed diam nonummy nibh euismod tincidunt ut laoreet dolore magna aliquam</div></div>
    <div class="card" style="left:81px;top:39px;background:var(--grey-dark)"><div class="copy">Lorem ipsum dolor sit amet, consectetuer adipiscing elit, sed diam nonummy nibh euismod tincidunt ut laoreet dolore magna aliquam</div></div>
    <div class="card" style="left:152px;top:39px;background:var(--grey)"><div class="copy">Lorem ipsum dolor sit amet, consectetuer adipiscing elit, sed diam nonummy nibh euismod tincidunt ut laoreet dolore magna aliquam</div></div>
    <div class="card-disc" style="left:28px;top:25px;background:var(--navy)"><svg><use href="#i-notes"/></svg></div>
    <div class="card-disc" style="left:99px;top:25px;background:var(--grey-dark)"><svg><use href="#i-piano"/></svg></div>
    <div class="card-disc" style="left:170px;top:25px;background:var(--grey)"><svg><use href="#i-leaf"/></svg></div>
  </section>

  <!-- Welcome text -->
  <section class="slide slide-welcome" style="left:469px;top:672px;width:223px;height:126px">
    <div class="photo" role="img" aria-label="Photo of a calm portrait framed by green leaves" style="left:26px;top:0;width:85px;height:126px;background:linear-gradient(120deg,#dfe6dd 0%,#b7c9a8 30%,#3f8a3a 60%,#1f4d22 100%)"></div>
    <div class="mark light" style="left:64px;top:96px;width:9px;height:9px"></div>
    <div class="wordmark light" style="left:26px;width:85px;top:109px"><span class="name" style="font-size:5px;letter-spacing:1.8px">LANTERN OAK</span><span class="sub" style="font-size:2.2px">AND BARRELS</span></div>
    <div class="title" style="left:129px;top:15px">WELCOME TEXT</div>
    <div class="rule" style="left:129px;top:27px"></div>
    <div class="copy" style="left:129px;top:38px;width:62px">Lorem ipsum dolor sit amet, consectetuer adipiscing elit, sed diam nonummy nibh euismod tincidunt ut laoreet dolore magna aliquam erat volutpat. Ut wisi enim ad minim veniam, quis nostrud exerci tation ullamcorper suscipit lobortis nisl ut aliquip ex ea commodo consequat. Duis autem vel eum iriure dolor in hendrerit</div>
    <div class="spine" style="left:210px;top:0;height:126px"></div>
    <div class="badge" style="left:201px;top:9px"></div>
    <div class="dot" style="left:4px;top:115px"></div>
  </section>

  <!-- Goals -->
  <section class="slide slide-goals" style="left:7px;top:805px;width:223px;height:126px">
    <div style="left:112px;top:14px;width:96px;height:96px;border-radius:50%;border:9px solid #ececec"></div>
    <div class="spine" style="left:12px;top:0;height:126px"></div>
    <div class="badge" style="left:3px;top:9px"></div>
    <div class="title" style="left:27px;top:15px">OUR GOALS OR BULLET POINT TEXT HERE</div>
    <div class="rule" style="left:27px;top:27px"></div>
    <ul class="bullets" style="left:24px;top:38px;width:170px">
      <li>Lorem ipsum dolor sit amet, consectetuer adipiscing elit, sed diam nonummy nibh euismod tincidunt ut laoreet dolore magna aliquam erat volutpat.</li>
      <li>Lorem ipsum dolor sit amet, consectetuer adipiscing elit, sed diam nonummy nibh euismod tincidunt ut laoreet dolore magna aliquam erat volutpat.</li>
      <li>Lorem ipsum dolor sit amet, consectetuer adipiscing elit, sed diam nonummy nibh euismod tincidunt ut laoreet dolore magna aliquam erat volutpat.</li>
      <li>Lorem ipsum dolor sit amet, consectetuer adipiscing elit, sed diam nonummy nibh euismod tincidunt ut laoreet dolore magna aliquam erat volutpat.</li>
      <li>Lorem ipsum dolor sit amet, consectetuer adipiscing elit, sed diam nonummy nibh euismod tincidunt ut laoreet dolore magna aliquam erat volutpat.</li>
    </ul>
    <div class="dot" style="left:213px;top:115px"></div>
  </section>

  <!-- Soul -->
  <section class="slide slide-soul" style="left:238px;top:805px;width:223px;height:126px">
    <div class="photo" role="img" aria-label="Photo of balanced stones by the sea at dusk" style="left:0;top:0;width:223px;height:126px;background:linear-gradient(180deg,#5d7fa8 0%,#a9b6c2 30%,#8a8d90 55%,#5a5a58 80%,#3b3a38 100%)"></div>
    <svg class="blob" viewBox="0 0 223 126" aria-hidden="true"><path d="M128 0C96 30 96 96 128 126L223 126L223 0Z" fill="#4b4d5a" opacity=".55"/></svg>
    <div class="spine light" style="left:131px;top:17px;height:93px"></div>
    <div class="title light" style="left:141px;top:15px">SOUL</div>
    <div class="rule light" style="left:141px;top:27px"></div>
    <div class="copy light" style="left:141px;top:38px;width:62px">Lorem ipsum dolor sit amet, consectetuer adipiscing elit, sed diam nonummy nibh euismod tincidunt ut laoreet dolore magna aliquam erat volutpat. Ut wisi enim ad minim veniam, quis nostrud exerci tation ullamcorper suscipit lobortis nisl ut aliquip ex ea commodo consequat. Duis autem vel eum iriure dolor in hendrerit</div>
    <div class="mark light" style="left:196px;top:103px;width:8px;height:8px;border-width:1px"></div>
    <div class="wordmark light" style="left:170px;width:60px;top:113px"><span class="name" style="font-size:4.4px;letter-spacing:1.5px">LANTERN OAK</span><span class="sub" style="font-size:2px">AND BARRELS</span></div>
  </section>

  <!-- Two columns -->
  <section class="slide slide-two-columns" style="left:469px;top:805px;width:223px;height:126px">
    <div class="title" style="left:8px;top:10px">LOREM IPSUM</div>
    <div class="copy navy" style="left:8px;top:24px;width:58px">Lorem ipsum dolor sit amet, consectetuer adipiscing elit, sed diam nonummy nibh euismod tincidunt ut laoreet dolore magna aliquam erat volutpat. Ut wisi enim ad minim veniam, quis nostrud exerci tation ullamcorper suscipit lobortis nisl ut aliquip ex ea commodo consequat. Duis autem vel eum iriure dolor in hendrerit</div>
    <div class="photo" role="img" aria-label="Photo of lit candles in soft light" style="left:67px;top:0;width:41px;height:84px;background:linear-gradient(180deg,#e9e6ec 0%,#c9c4d2 40%,#f2c978 60%,#6d6879 100%)"></div>
    <div class="photo" role="img" aria-label="Photo of lit candles on a dark table" style="left:110px;top:30px;width:39px;height:96px;background:linear-gradient(180deg,#3a3540 0%,#d9d2dc 35%,#f3c66a 60%,#2b2830 100%)"></div>
    <div class="mark" style="left:82px;top:96px;width:9px;height:9px"></div>
    <div class="wordmark" style="left:54px;width:64px;top:109px"><span class="name" style="font-size:5px;letter-spacing:1.8px">LANTERN OAK</span><span class="sub" style="font-size:2.2px">AND BARRELS</span></div>
    <div class="title" style="right:5px;top:10px">LOREM IPSUM</div>
    <div class="copy" style="right:5px;top:24px;width:56px;text-align:right">Lorem ipsum dolor sit amet, consectetuer adipiscing elit, sed diam nonummy nibh euismod tincidunt ut laoreet dolore magna aliquam erat volutpat. Ut wisi enim ad minim veniam, quis nostrud exerci tation ullamcorper suscipit lobortis nisl ut aliquip ex ea commodo consequat. Duis autem vel eum iriure dolor in hendrerit</div>
    <div style="left:143px;top:103px;width:75px;height:12px;background:var(--navy)"></div>
  </section>

  <!-- Infographic -->
  <section class="slide slide-infographic" style="left:7px;top:938px;width:454px;height:259px">
    <svg class="blob" viewBox="0 0 454 259" aria-hidden="true">
      <g fill="none" stroke="var(--line-grey)" stroke-width="1.4" stroke-dasharray="5 4">
        <circle cx="227" cy="131" r="70"/>
        <path d="M136 55L173 86M314 57L281 86M121 131L157 131M330 131L297 131M136 204L173 176M314 204L281 176"/>
      </g>
      <circle cx="227" cy="131" r="48" fill="none" stroke="var(--navy)" stroke-width="7"/>
    </svg>
    <div class="wordmark" style="left:187px;width:80px;top:124px"><span class="name" style="font-size:7px;letter-spacing:1.4px">LANTERN OAK</span><span class="sub" style="font-size:3.4px;letter-spacing:1.2px;margin-top:2px">AND BARRELS</span></div>

    <div class="info-disc" style="left:94px;top:16px"><svg><use href="#i-apple"/></svg></div>
    <div class="info-disc" style="left:309px;top:18px"><svg><use href="#i-flame"/></svg></div>
    <div class="info-disc" style="left:73px;top:107px"><svg><use href="#i-drops"/></svg></div>
    <div class="info-disc" style="left:330px;top:107px"><svg><use href="#i-leaf"/></svg></div>
    <div class="info-disc" style="left:94px;top:195px"><svg><use href="#i-notes"/></svg></div>
    <div class="info-disc" style="left:309px;top:195px"><svg><use href="#i-move"/></svg></div>

    <div style="right:365px;top:18px;text-align:right"><div class="info-head">LOREM IPSUM</div><div class="info-copy">Lorem ipsum dolor sit<br>amet, consectetuer<br>adipiscing elit.</div></div>
    <div style="left:361px;top:18px"><div class="info-head">LOREM IPSUM</div><div class="info-copy">Lorem ipsum dolor sit<br>amet, consectetuer<br>adipiscing elit.</div></div>
    <div style="right:386px;top:104px;text-align:right"><div class="info-head">LOREM IPSUM</div><div class="info-copy">Lorem ipsum dolor<br>sit amet, consec-<br>tetuer adipiscing</div></div>
    <div style="left:380px;top:103px"><div class="info-head">LOREM IPSUM</div><div class="info-copy">Lorem ipsum dolor<br>sit amet, consec-<br>tetuer adipiscing</div></div>
    <div style="right:367px;top:191px;text-align:right"><div class="info-head">LOREM IPSUM</div><div class="info-copy">Lorem ipsum dolor<br>sit amet, consec-<br>tetuer adipiscing</div></div>
    <div style="left:358px;top:191px"><div class="info-head">LOREM IPSUM</div><div class="info-copy">Lorem ipsum dolor sit<br>amet, consectetuer<br>adipiscing elit.</div></div>
  </section>

  <!-- Music (blob) -->
  <section class="slide slide-music-feature" style="left:469px;top:938px;width:223px;height:126px">
    <div class="photo" role="img" aria-label="Photo of an acoustic guitar close to the strings" style="left:0;top:0;width:223px;height:126px;background:radial-gradient(ellipse at 45% 60%,#2a1a10 0%,#6b3a17 18%,#c27a35 40%,#8a4f22 65%,#2b2233 100%)"></div>
    <svg class="blob" viewBox="0 0 223 126" aria-hidden="true"><path d="M0 50C30 40 60 60 70 90C75 110 80 120 84 126L0 126Z" fill="var(--navy)"/><path d="M130 0C135 20 160 28 175 40C195 55 205 75 223 85L223 0Z" fill="var(--navy)" opacity=".92"/></svg>
    <div class="title light" style="right:7px;top:9px">MUSIC</div>
    <div class="copy light" style="right:7px;top:23px;width:44px;text-align:right">Lorem ipsum dolor sit amet, consectetuer adipiscing elit, sed diam nonummy nibh euismod tincidunt ut laoreet dolore magna aliquam</div>
    <div class="disc" style="left:186px;top:69px"><svg><use href="#i-notes"/></svg></div>
    <div class="mark light" style="left:33px;top:89px;width:9px;height:9px"></div>
    <div class="wordmark light" style="left:6px;width:64px;top:101px"><span class="name" style="font-size:5px;letter-spacing:1.8px">LANTERN OAK</span><span class="sub" style="font-size:2.2px">AND BARRELS</span></div>
  </section>

  <!-- Thank you -->
  <section class="slide slide-thank-you" style="left:469px;top:1071px;width:223px;height:126px">
    <div class="photo" role="img" aria-label="Photo of a person in an infinity pool looking out to sea" style="left:0;top:0;width:223px;height:126px;background:linear-gradient(180deg,#ffffff 0%,#eef3f8 30%,#bcd2e6 50%,#6c9cc7 62%,#3c6f9f 82%,#2a4f78 100%)"></div>
    <div style="left:0;top:113px;width:223px;height:13px;background:rgba(20,35,60,.55)"></div>
    <div class="spine" style="left:12px;top:0;height:126px"></div>
    <div class="badge" style="left:3px;top:9px"></div>
    <div class="title" style="left:28px;top:12px;font-size:13px">THANK YOU</div>
    <div class="rule" style="left:28px;top:28px"></div>
    <div class="mark" style="left:187px;top:11px;width:9px;height:9px"></div>
    <div class="wordmark" style="left:159px;width:64px;top:24px"><span class="name" style="font-size:5px;letter-spacing:1.8px">LANTERN OAK</span><span class="sub" style="font-size:2.2px">AND BARRELS</span></div>
    <div class="contact" style="left:18px;top:116px"><svg><use href="#i-globe"/></svg>www.yourwebsite.com</div>
    <div class="contact" style="left:74px;top:116px"><svg><use href="#i-phone"/></svg>123.456.7890</div>
    <div class="contact" style="left:115px;top:116px"><svg><use href="#i-mail"/></svg>Your email@.com</div>
    <div class="contact" style="left:160px;top:114.5px"><svg><use href="#i-pin"/></svg><span>Your address , PO Box 5059,<br>Street road, CA 00000</span></div>
  </section>

</main>
</body>
</html>
```